Sleek, Professional Business Card Design Needed

Business Cards - Logo Attached.

We are a solar consulting company. We are national and want our cards to represent the professional high quality products that we offer.

Industry/Entity Type

Business

Contact Information for Business Card

n/a

Requirements
Must have
• Design
• Name
• Position
• Number
• Email
• Address
Should not have
• Not be too crowded

```html
<!DOCTYPE html>
<html lang="en">
<head>
<meta charset="utf-8">
<title>Brightfield Solar – Business Card</title>
<link href="https://fonts.googleapis.com/css2?family=Questrial&family=Open+Sans:wght@400;600&display=swap" rel="stylesheet">
<style>
  :root {
    --backdrop: #3b322d;
    --card: #1c1c1d;
    --brand-blue: #1e90d8;
    --brand-green: #8dc63f;
    --text-grey: #a4a4a6;
    --emboss: #3a3a3c;
  }
  * { margin: 0; padding: 0; box-sizing: border-box; }
  html, body { width: 1200px; height: 716px; overflow: hidden; }
  body {
    background: var(--backdrop);
    position: relative;
    font-family: "Open Sans", sans-serif;
  }
  .card {
    position: absolute;
    top: 213px;
    width: 500px;
    height: 290px;
    background: var(--card);
    overflow: hidden;
    box-shadow: 0 10px 24px rgba(0,0,0,0.45);
  }
  .card--front { left: 90px; }
  .card--back { left: 610px; }
  .emboss-ring {
    position: absolute;
    top: 0;
    width: 500px;
    height: 290px;
  }
  .card--front .emboss-ring { left: 0; }
  .card--back .emboss-ring { left: 0; }
  .brand {
    position: absolute;
    display: flex;
    align-items: center;
    gap: 10px;
  }
  .brand__dot {
    width: 34px;
    height: 34px;
    border-radius: 50%;
    background: var(--brand-green);
  }
  .brand__name {
    font-family: "Questrial", sans-serif;
    font-size: 22px;
    letter-spacing: 1px;
    color: var(--brand-blue);
    text-transform: uppercase;
  }
  .card--front .brand { left: 34px; top: 30px; }
  .card--back .brand { right: 34px; bottom: 34px; }
  .card--back .brand__name { font-size: 28px; }
  .card--back .brand__dot { width: 44px; height: 44px; }
  .contact {
    position: absolute;
    left: 34px;
    top: 100px;
    color: var(--text-grey);
    font-size: 12px;
    line-height: 1.55;
  }
  .contact__name {
    color: var(--brand-blue);
    font-weight: 600;
    font-size: 15px;
    text-transform: uppercase;
    letter-spacing: 0.5px;
  }
  .contact__role { margin-bottom: 8px; }
  .contact__line { display: flex; align-items: center; gap: 7px; }
  .contact__icon { width: 10px; height: 10px; flex: none; }
</style>
</head>
<body>
  <section class="card card--front">
    <svg class="emboss-ring" viewBox="0 0 500 290" aria-hidden="true">
      <circle cx="510" cy="145" r="135" fill="none" stroke="var(--emboss)" stroke-width="10"/>
    </svg>
    <div class="brand">
      <span class="brand__dot"></span>
      <span class="brand__name">Brightfield Solar</span>
    </div>
    <div class="contact">
      <p class="contact__name">Dana Whitcombe</p>
      <p class="contact__role">Managing Director</p>
      <p class="contact__line">
        <svg class="contact__icon" viewBox="0 0 10 10"><rect width="10" height="10" rx="2" fill="var(--brand-green)"/><path d="M3 2.5c-.6 1.8 1.4 4.6 4.5 5l.5-1.3-1.5-.7-.6.6C5 5.6 4.3 4.9 3.9 4l.6-.6L3.8 2z" fill="var(--card)"/></svg>
        +000 000 0000
      </p>
      <p class="contact__line">
        <svg class="contact__icon" viewBox="0 0 10 10"><rect width="10" height="10" rx="2" fill="var(--brand-green)"/><path d="M2 3h6v4H2zM2 3l3 2.2L8 3" fill="none" stroke="var(--card)" stroke-width="0.9"/></svg>
        dana@brightfieldsolar.com
      </p>
      <p class="contact__line">118 Harbor Lane, Portland, ME 04101</p>
    </div>
  </section>

  <section class="card card--back">
    <svg class="emboss-ring" viewBox="0 0 500 290" aria-hidden="true">
      <circle cx="-10" cy="145" r="135" fill="none" stroke="var(--emboss)" stroke-width="10"/>
    </svg>
    <div class="brand">
      <span class="brand__dot"></span>
      <span class="brand__name">Brightfield Solar</span>
    </div>
  </section>
</body>
</html>
```